Brant Ocheltree | Inbound Marketing

Need a logo for a company that fills the need of creating a consistent stream of warm sales leads and revenue (via building of a sales funnel) to companies who either do not have sales teams or use outmoded outbound sales strategy to address the company bottom line. This includes Inbound marketing, SEO, content marketing strategy

Target Market(s)

Small to Medium Size Businesses, who are willing to spend thousands or tens of thousands of dollars on avertising.

Industry/Entity Type

It Company

Contact Information for Business Card

Content Strategy | PPC | SEO | Local Social & SEO
512.604.7731
brantocheltree@mailvista.net

Logo Text

Look Inward to Gain Outward

Font styles to use
Sans Serif

Requirements
Nice to have
• I am partial to funnels in natural phenomena (tornados, whirlpools, hurricanes, black holes, spiral galaxies) but this is not a deal breaker. In fact, I don't want to intimidate anybody and seeing photos and artist representation are somewhat unsettling to me as to their vastness and darkness

```html
<!DOCTYPE html>
<html lang="en">
<head>
<meta charset="utf-8">
<title>Brant Ocheltree | Business Cards</title>
<link rel="stylesheet" href="https://fonts.googleapis.com/css2?family=Mulish:wght@400;800&display=swap">
<style>
  :root {
    --backdrop: #e8e8ea;
    --card-dark: #0c0c0c;
    --card-light: #ffffff;
    --ink-light: #f2f2f2;
    --ink-dark: #111111;
    --rule: #6a6a6a;
    --mark-faint: #1f1f1f;
  }
  html, body {
    margin: 0;
    padding: 0;
    width: 1200px;
    height: 1200px;
    overflow: hidden;
    background: var(--backdrop);
    font-family: "Mulish", sans-serif;
  }
  .canvas {
    position: relative;
    width: 1200px;
    height: 1200px;
  }
  .card {
    position: absolute;
    width: 560px;
    height: 320px;
    border-radius: 4px;
    box-shadow: 0 6px 18px rgba(0,0,0,0.15);
    overflow: hidden;
  }
  /* Contact side */
  .card--contact {
    left: 580px;
    top: 230px;
    background: var(--card-dark);
    color: var(--ink-light);
  }
  .card--contact > * {
    position: absolute;
    z-index: 1;
  }
  .card--contact .faint-mark {
    z-index: 0;
    right: -40px;
    top: 70px;
    width: 230px;
    height: 230px;
  }
  .card--contact .holder-name {
    left: 36px;
    top: 30px;
    margin: 0;
    font-size: 38px;
    font-weight: 800;
    letter-spacing: 0.2px;
  }
  .contact-list {
    left: 36px;
    top: 138px;
    margin: 0;
    padding: 0;
    list-style: none;
    font-size: 17px;
    line-height: 27px;
  }
  .contact-list li {
    display: flex;
    align-items: center;
    gap: 9px;
  }
  .contact-list svg {
    width: 14px;
    height: 14px;
    flex: none;
  }
  .contact-rule {
    left: 36px;
    top: 230px;
    width: 440px;
    height: 1px;
    background: var(--rule);
  }
  .services {
    left: 36px;
    top: 242px;
    margin: 0;
    font-size: 16.5px;
    letter-spacing: 0.3px;
  }
  /* Brand side */
  .card--brand {
    left: 60px;
    top: 660px;
    background: var(--card-light);
    color: var(--ink-dark);
  }
  .brand-lockup {
    position: absolute;
    inset: 0;
    display: flex;
    flex-direction: column;
    align-items: center;
    justify-content: center;
    gap: 6px;
  }
  .brand-dot {
    width: 54px;
    height: 54px;
    border-radius: 50%;
    background: var(--ink-dark);
    margin-bottom: 6px;
  }
  .brand-name {
    margin: 0;
    font-size: 34px;
    font-weight: 800;
    line-height: 1;
  }
  .brand-url {
    margin: 0;
    font-size: 13px;
    letter-spacing: 4.2px;
  }
</style>
</head>
<body>
<main class="canvas">

  <section class="card card--contact">
    <svg class="faint-mark" viewBox="0 0 230 230" aria-hidden="true">
      <circle cx="115" cy="115" r="105" fill="none" stroke="var(--mark-faint)" stroke-width="10"/>
    </svg>
    <h1 class="holder-name">Brant Ocheltree</h1>
    <ul class="contact-list">
      <li>
        <svg viewBox="0 0 16 16" aria-hidden="true"><path fill="currentColor" d="M1 5c0-2 2-3 7-3s7 1 7 3v1h-3V5H4v1H1zM3 8l2-2h6l2 2v6H3zm5 1.5a2 2 0 1 0 0 4 2 2 0 0 0 0-4z"/></svg>
        512.604.7731
      </li>
      <li>
        <svg viewBox="0 0 16 16" aria-hidden="true"><g fill="none" stroke="currentColor" stroke-width="1.3"><circle cx="8" cy="8" r="6.5"/><ellipse cx="8" cy="8" rx="3" ry="6.5"/><path d="M1.5 8h13M2.5 4.5h11M2.5 11.5h11"/></g></svg>
        www.ocheltreeinbound.com
      </li>
      <li>
        <svg viewBox="0 0 16 16" aria-hidden="true"><g fill="none" stroke="currentColor" stroke-width="1.3"><rect x="1" y="3" width="14" height="10"/><path d="M1 3l7 6 7-6"/></g></svg>
        brantocheltree@mailvista.net
      </li>
    </ul>
    <div class="contact-rule"></div>
    <p class="services">Content Strategy | PPC | SEO | Local Social &amp; SEO</p>
  </section>

  <section class="card card--brand">
    <div class="brand-lockup">
      <div class="brand-dot"></div>
      <p class="brand-name">Brant Ocheltree</p>
      <p class="brand-url">www.ocheltreeinbound.com</p>
    </div>
  </section>

</main>
</body>
</html>
```